Private Security Company Business Card and Logo Design

Looking for a modern conservative business card design for our new private security company Harbor Ridge Guard Co., Inc. or HRGC for short.
Private Security Services. The current logo we have is not very good and honestly would like a sharp logo for the card instead of using the one we have now. Open to ideas. I am easy just looking for something nicer then what I can personally design on cardmillo. I searched on zintoo for Security Company business cards went to images and found some nice designs that were made here.

Target Market(s)

Security Services

Industry/Entity Type

Business

Contact Information for Business Card

Harbor Ridge Guard Co., Inc.
President, cell,office,fax,email, website,
Logo etc, whatever is needed for a standard business card
Can provide personal Information later.

Colors
0556a4
ffffff
474747

Requirements
Must have
• Modern but conservative,
Nice to have
• color choices
• Blue, white, Grey

```html
<!DOCTYPE html>
<html lang="en">
<head>
<meta charset="utf-8">
<title>Harbor Ridge Guard Co. Business Card</title>
<link rel="stylesheet" href="https://fonts.googleapis.com/css2?family=Open+Sans:wght@400;700&display=swap">
<style>
  :root {
    --ink: #000000;
    --paper: #ffffff;
    --stage: #e9e7e4;
    --text: #1a1a1a;
    --brand-blue: #0556a4;
    --brand-grey: #474747;
  }
  html, body {
    margin: 0;
    width: 1200px;
    height: 900px;
    overflow: hidden;
    background: var(--stage);
    font-family: "Open Sans", Arial, sans-serif;
  }
  .stage { position: relative; width: 1200px; height: 900px; }

  .card {
    position: absolute;
    border-radius: 16px;
    overflow: hidden;
    box-shadow: 0 6px 18px rgba(0,0,0,0.18);
  }
  .card--front { left: 78px; top: 35px; width: 588px; height: 363px; background: var(--paper); }
  .card--back { left: 389px; top: 507px; width: 565px; height: 348px; background: var(--ink); }

  .band { position: absolute; left: 0; right: 0; }
  .card--front .band { top: 62px; height: 99px; background: var(--ink); }
  .card--back .band { top: 80px; height: 97px; background: var(--paper); }

  .emblem {
    position: absolute;
    border-radius: 50%;
    display: flex;
    flex-direction: column;
    align-items: center;
    justify-content: center;
    font-weight: 700;
  }
  .card--front .emblem {
    left: 204px; top: 19px; width: 186px; height: 186px;
    background: var(--paper); color: var(--ink);
  }
  .card--back .emblem {
    left: 197px; top: 40px; width: 172px; height: 172px;
    background: var(--ink); color: var(--paper);
  }
  .emblem__initials { font-size: 34px; line-height: 1; letter-spacing: 0.5px; }
  .emblem__name { font-size: 8.5px; margin-top: 4px; }

  .holder {
    position: absolute;
    right: 313px;
    top: 234px;
    text-align: right;
    color: var(--text);
  }
  .holder__name { font-size: 24px; line-height: 30px; }
  .holder__title { font-size: 16px; line-height: 20px; }
  .holder__address { font-size: 16px; line-height: 19px; margin-top: 12px; }

  .contacts {
    position: absolute;
    left: 314px;
    top: 236px;
    margin: 0; padding: 0;
    list-style: none;
    color: var(--text);
    font-size: 16px;
  }
  .contacts li { display: flex; align-items: center; height: 24.5px; }
  .contacts svg { width: 12px; height: 12px; margin-right: 10px; fill: var(--text); }
</style>
</head>
<body>
<main class="stage">

  <section class="card card--front" aria-label="Business card front">
    <div class="band"></div>
    <div class="emblem">
      <span class="emblem__initials">HRGC</span>
      <span class="emblem__name">Harbor Ridge Guard Co., Inc.</span>
    </div>

    <div class="holder">
      <div class="holder__name">Daniel Mercer</div>
      <div class="holder__title">Managing Director</div>
      <div class="holder__address">12345, Address Goes Here<br>Country Name, 123456</div>
    </div>

    <ul class="contacts">
      <li>
        <svg viewBox="0 0 12 12" aria-hidden="true"><path d="M2.4 0.6 4.3 2.8 3.4 4.2c.8 1.7 2.3 3.2 4 4l1.4-.9 2.2 1.9-.9 2.1C5.6 11.3.7 6.4.3 1.5z"/></svg>
        (044)-456-7890
      </li>
      <li>
        <svg viewBox="0 0 12 12" aria-hidden="true"><path d="M3 0h5v3H3zM0 3.5h12V12H0zM2 5v1.5h1.5V5zm3 0v1.5h1.5V5zm3 0v1.5h2V5zM2 8v1.5h1.5V8zm3 0v1.5h1.5V8zm3 0v1.5h2V8z" fill-rule="evenodd"/></svg>
        123-456-7890
      </li>
      <li>
        <svg viewBox="0 0 12 12" aria-hidden="true"><path d="M0 2h12v8H0zm1.2 1.2v.3L6 6.7l4.8-3.2v-.3zm0 1.6V8.8h9.6V4.8L6 8z" fill-rule="evenodd"/></svg>
        info@youremail.com
      </li>
      <li>
        <svg viewBox="0 0 12 12" aria-hidden="true"><circle cx="6" cy="6" r="6"/><path d="M3 3.5c1 .2 1.6 1 1.3 2-.3.8.6 1.3.4 2.4L4 10C2.6 9 2 7.6 2 6c0-1 .4-1.8 1-2.5zm4.5-1.6c1.3.3 2.3 1.1 2.8 2.3-.9.2-1.6-.4-2.2.1-.6.6-1.4.1-1.2-.8.2-.7.5-1 .6-1.6z" fill="#fff"/></svg>
        www.website.com
      </li>
    </ul>
  </section>

  <section class="card card--back" aria-label="Business card back">
    <div class="band"></div>
    <div class="emblem">
      <span class="emblem__initials">HRGC</span>
      <span class="emblem__name">Harbor Ridge Guard Co., Inc.</span>
    </div>
  </section>

</main>
</body>
</html>
```